Counselling business requires poster

I require a poster to promote my counselling and coaching business I will be placing these in doctors surgery's and clinics etc.
This business is centred around helping people work through emotional issues. We provided one on one sessions which help enhance peoples lives by assisting them in overcoming their fears, obsessions, insecurities etc.

We offer support in a broad range of areas:

- Eating disorders & weight managment
- Depression
- Marriage and relationship issues
- Anxiety
- Victims of physical, verbal and/or social abuse

We want our poster to be representative of the positive, warm and welcoming atmosphere we provide.

Our motto, 'One step at a time', is symbolic of our approach and how we help our clients to tackle their problems bit by bit.

The flyer I have uploaded is just some information on what we offer

Thankyou for your designs I am taking them into consideration and will inform you of any decision.

```html
<!DOCTYPE html>
<html lang="en">
<head>
<meta charset="utf-8">
<title>One step at a time – Stepwise counselling poster</title>
<link rel="stylesheet" href="https://fonts.googleapis.com/css2?family=Jost:wght@700&display=swap">
<style>
  :root {
    --bg-centre: #ffb902;
    --bg-mid: #f3a000;
    --bg-edge: #dc7c02;
    --accent-red: #ff3b10;
    --tick-orange: #ff7f0c;
    --box-orange: #ff7f07;
  }
  * { margin: 0; padding: 0; box-sizing: border-box; }
  html, body {
    width: 848px;
    height: 1200px;
    overflow: hidden;
  }
  body {
    font-family: "Jost", "Century Gothic", sans-serif;
  }
  .poster {
    position: relative;
    width: 848px;
    height: 1200px;
    overflow: hidden;
    background: radial-gradient(circle at 380px 600px,
      var(--bg-centre) 0%,
      var(--bg-mid) 45%,
      var(--bg-edge) 100%);
  }
  .checklist {
    position: absolute;
    inset: 0;
    width: 848px;
    height: 1200px;
  }
  .motto {
    position: absolute;
    left: 358px;
    top: 366px;
    color: var(--accent-red);
    font-weight: 700;
    line-height: 1;
  }
  .motto__line--first {
    display: block;
    font-size: 92px;
    letter-spacing: -1px;
  }
  .motto__line--second {
    display: block;
    font-size: 80px;
    letter-spacing: -0.5px;
    margin-top: -6px;
  }
  .brand {
    position: absolute;
    right: 30px;
    bottom: 26px;
    color: var(--accent-red);
    font-weight: 700;
    font-size: 20px;
    line-height: 1;
  }
</style>
</head>
<body>
  <main class="poster">
    <svg class="checklist" viewBox="0 0 848 1200" aria-hidden="true">
      <rect class="checklist__box checklist__box--done" x="117" y="355" width="202" height="202" fill="var(--accent-red)"/>
      <path class="checklist__tick" fill="var(--tick-orange)"
        d="M150,429 L179,407 Q205,432 222,468 Q281,350 387,292 Q291,372 244,501 L205,524 Q190,471 150,429 Z"/>
      <rect class="checklist__box" x="147" y="594" width="141" height="141" fill="var(--box-orange)"/>
      <rect class="checklist__box" x="147" y="774" width="141" height="141" fill="var(--box-orange)"/>
    </svg>

    <h1 class="motto">
      <span class="motto__line--first">one step</span>
      <span class="motto__line--second">at a time</span>
    </h1>

    <p class="brand">stepwise</p>
  </main>
</body>
</html>
```